stationary for hygienic company

We need a stationary design for hygienic company which provides public high end sanitary products and high end public lavatory.
We need a fresh and clean style stationary
we want the following things:
* logo (redesigned in eps/vector)
* Letterhead (with company details)
* letterhead (without company details)
* Business card
* note block
* ballpoint
* etcetera (a complete package)

```html
<!DOCTYPE html>
<html lang="fr">
<head>
<meta charset="utf-8">
<title>Velmira — Stationery Set</title>
<link rel="stylesheet" href="https://fonts.googleapis.com/css2?family=Jost:wght@400&family=Questrial&display=swap">
<style>
  :root {
    --paper: #ffffff;
    --backdrop: #ffffff;
    --ink: #111111;
    --edge: #8a8a8a;
    --magenta: #e6087e;
    --navy: #120a73;
    --cyan: #12a9ea;
    --window: #d6d6d6;
    --faint-mark: #dcdbe2;
  }
  * { box-sizing: border-box; margin: 0; padding: 0; }
  html, body {
    width: 1200px; height: 1200px; overflow: hidden;
    background: var(--backdrop);
  }
  .canvas { position: relative; width: 1200px; height: 1200px; }

  .brand { text-align: center; color: var(--ink); }
  .brand-name {
    font-family: "Jost", sans-serif; font-weight: 400;
    letter-spacing: 0.04em; line-height: 1;
  }
  .brand-tagline {
    font-family: "Questrial", sans-serif; line-height: 1.1;
  }

  /* Letterhead */
  .letterhead {
    position: absolute; left: 388px; top: 82px;
    width: 748px; height: 1054px;
    background: var(--paper); border: 1.5px solid var(--edge);
  }
  .letterhead .brand { position: absolute; left: 520px; top: 108px; width: 180px; }
  .letterhead .brand-name { font-size: 40px; }
  .letterhead .brand-tagline { font-size: 11px; }

  /* Business card */
  .business-card {
    position: absolute; left: 40px; top: 318px;
    width: 598px; height: 375px;
    background: var(--paper); border: 1.5px solid #333;
    border-radius: 14px; overflow: hidden;
  }
  .business-card .brand { position: absolute; left: 199px; top: 145px; width: 200px; }
  .business-card .brand-name { font-size: 42px; }
  .business-card .brand-tagline { font-size: 11px; }
  .card-stripe { position: absolute; left: 0; bottom: 0; width: 598px; height: 10px; }

  /* Envelope */
  .envelope {
    position: absolute; left: 146px; top: 843px;
    width: 889px; height: 330px;
    background: var(--paper); border: 1.5px solid #333;
  }
  .envelope .brand { position: absolute; left: 40px; top: 70px; width: 155px; }
  .envelope .brand-name { font-size: 34px; }
  .envelope .brand-tagline { font-size: 9.5px; }
  .address-window {
    position: absolute; left: 43px; top: 198px;
    width: 312px; height: 87px;
    border: 4px solid var(--window);
  }
  .envelope-watermark {
    position: absolute; left: 560px; top: 95px;
    font-family: "Jost", sans-serif; font-weight: 400;
    font-size: 54px; color: var(--faint-mark); letter-spacing: 0.04em;
  }
</style>
</head>
<body>
<main class="canvas">

  <section class="letterhead" aria-label="Letterhead">
    <div class="brand">
      <div class="brand-name">Velmira</div>
      <div class="brand-tagline">Boutique Hygienique<br>Marque deposee</div>
    </div>
  </section>

  <section class="business-card" aria-label="Business card">
    <div class="brand">
      <div class="brand-name">Velmira</div>
      <div class="brand-tagline">Boutique Hygienique<br>Marque deposee</div>
    </div>
    <svg class="card-stripe" viewBox="0 0 598 10" preserveAspectRatio="none" aria-hidden="true">
      <polygon points="0,0 180,0 186,10 0,10" fill="var(--magenta)"/>
      <polygon points="180,0 390,0 396,10 186,10" fill="var(--navy)"/>
      <polygon points="390,0 598,0 598,10 396,10" fill="var(--cyan)"/>
    </svg>
  </section>

  <section class="envelope" aria-label="Envelope">
    <div class="brand">
      <div class="brand-name">Velmira</div>
      <div class="brand-tagline">Boutique Hygienique<br>Marque deposee</div>
    </div>
    <div class="address-window"></div>
    <div class="envelope-watermark">Velmira</div>
  </section>

</main>
</body>
</html>
```